Business Card Design Project

We are not a new company, but renamed to "Norvanta Kitchens" last year. We specialize in modern high-end cabinetry imports. We would like to communicate a sense of quality and cutting edge technology. Ideally the design would incorporate our logo colors, silver, red and preferably a black, matte background. Though we are open to suggestions.
Logo is attached.
Edit: I have attached rough drafts of the previous cards, this way you will have all necessary content that needs to go on the cards.
Reason: We have received a lot of great designs, but due to the sheer number we couldn't respond to all. We will extend the deadline for another 7 days to finalize and provide feedback to designers.
Thank you for your hard work!
Industry/Entity Type
Business
Look and feel
Each slider illustrates characteristics of the customer's brand and the style your logo design should communicate.

```html
<!DOCTYPE html>
<html lang="en">
<head>
<meta charset="utf-8">
<title>Norvanta Kitchens – Business Card</title>
<link rel="stylesheet" href="https://fonts.googleapis.com/css2?family=Roboto:wght@400;500;700&display=swap">
<style>
  :root {
    --page-bg: #c9d3d1;
    --card-black: #141414;
    --card-black-2: #262626;
    --panel-grey: #8c8c8c;
    --panel-grey-light: #a3a3a3;
    --accent-red: #e21f26;
    --line-dark: #3a3a3a;
    --silver: #d6d6d6;
    --white: #ffffff;
    --muted: #e3e3e3;
  }
  * { box-sizing: border-box; margin: 0; padding: 0; }
  html, body {
    width: 1200px; height: 973px; overflow: hidden;
    background: var(--page-bg);
    font-family: "Roboto", Arial, sans-serif;
  }
  .sheet {
    width: 1200px; height: 973px;
    display: flex; flex-direction: column; align-items: center; justify-content: center;
    gap: 50px;
  }
  .card {
    position: relative;
    width: 720px; height: 411px;
    overflow: hidden;
    background: radial-gradient(ellipse at 40% 40%, var(--card-black-2), var(--card-black) 75%);
    box-shadow: 0 6px 18px rgba(0,0,0,0.25);
  }
  .card-wave { position: absolute; inset: 0; width: 100%; height: 100%; }

  .brand-name {
    position: absolute;
    display: flex; align-items: center; gap: 12px;
    color: var(--silver);
    font-weight: 500;
    text-transform: uppercase;
    letter-spacing: 2px;
    white-space: nowrap;
  }
  .brand-mark { display: block; background: var(--silver); }

  .card-front .brand-name { left: 40px; top: 44px; font-size: 30px; }
  .card-front .brand-mark { width: 22px; height: 22px; }

  .holder { position: absolute; left: 70px; top: 240px; color: var(--white); }
  .holder-name { font-size: 17px; font-weight: 700; letter-spacing: 0.5px; text-transform: uppercase; }
  .holder-role { font-size: 14px; color: var(--muted); margin-top: 2px; }

  .contact { position: absolute; right: 34px; top: 40px; color: var(--white); font-size: 15px; }
  .contact-list { list-style: none; text-align: left; }
  .contact-list li { display: flex; align-items: center; gap: 8px; line-height: 22px; }
  .contact-list svg { width: 13px; height: 13px; fill: var(--white); flex: none; }
  .contact-web { padding-left: 21px; }
  .contact-email { position: absolute; right: 34px; top: 190px; display: flex; align-items: center; gap: 8px; color: var(--white); font-size: 15px; }
  .contact-email svg { width: 14px; height: 11px; fill: var(--white); }
  .contact-address { position: absolute; right: 34px; top: 238px; color: var(--white); font-size: 15px; }

  .card-back .brand-name {
    left: 50%; top: 50%; transform: translate(-50%, -50%);
    font-size: 44px; letter-spacing: 3px;
  }
  .card-back .brand-mark { width: 30px; height: 30px; }
</style>
</head>
<body>
<main class="sheet">

  <section class="card card-front" aria-label="Business card front">
    <svg class="card-wave" viewBox="0 0 720 411" aria-hidden="true">
      <path d="M450 0 C 410 150, 340 285, 130 345 C 70 362, 25 372, 0 378 L 0 411 L 720 411 L 720 0 Z" fill="var(--panel-grey)"/>
      <path d="M450 0 C 410 150, 340 285, 130 345 C 70 362, 25 372, 0 378" fill="none" stroke="var(--line-dark)" stroke-width="6"/>
      <path d="M440 0 C 395 140, 320 270, 120 328 C 65 344, 25 352, 0 356" fill="none" stroke="var(--accent-red)" stroke-width="9"/>
      <path d="M470 0 C 440 120, 390 240, 240 320" fill="none" stroke="var(--panel-grey-light)" stroke-width="3" opacity="0.6"/>
    </svg>

    <div class="brand-name"><span class="brand-mark"></span>Norvanta Kitchens</div>

    <div class="holder">
      <p class="holder-name">Marcus Delvin</p>
      <p class="holder-role">Director</p>
    </div>

    <div class="contact">
      <ul class="contact-list">
        <li><svg viewBox="0 0 16 16"><path d="M3 1l3 3-2 2c1 2 3 4 5 5l2-2 3 3-2 3C6 14 2 10 1 3z"/></svg>403.555.0148</li>
        <li><svg viewBox="0 0 16 16"><path d="M4 1h8v4H4zM1 6h14v6h-3v3H4v-3H1zM5 10v4h6v-4z"/></svg>403.555.0193</li>
        <li><svg viewBox="0 0 16 16"><path d="M4 0h8v16H4zM5.5 2v10h5V2z"/></svg>403.555.0267</li>
        <li class="contact-web">norvantakitchens.ca</li>
      </ul>
    </div>
    <p class="contact-email"><svg viewBox="0 0 16 12"><path d="M0 0h16v12H0zM1.5 1.5L8 7l6.5-5.5z"/></svg>marcus@norvantakitchens.ca</p>
    <p class="contact-address">2150 - 84 Ave. Calgary, AB T2K 4R9</p>
  </section>

  <section class="card card-back" aria-label="Business card back">
    <div class="brand-name"><span class="brand-mark"></span>Norvanta Kitchens</div>
  </section>

</main>
</body>
</html>
```